Harbor 3 Engineering Career Fair Banner

We need a 2.5' x 6' Vertical Banner Design for our technology team based in San Francisco called "Harbor 3 - Data Discovery Studio". We sit within Meridian Crest Financial although the Meridian Crest name & logo doesn't need to be prominent in the design. Being a Data Discovery Studio, we have a strong focus in Machine Learning and Big Data. We're using the banner at an upcoming career fair to hire Data Scientists, Data Engineers, and Software Engineers. We would like to see designs that use the color green and incorporate the Harbor 3 logo (attached).
Target Market(s)
Graduate students at WPSB; specifically targeting CS, Mathematics, Statistics, Research students
Industry/Entity Type
Information Technology

```html
<!DOCTYPE html>
<html lang="en">
<head>
<meta charset="utf-8">
<title>Harbor 3 – Data Discovery Studio Career Fair Banner</title>
<link rel="stylesheet" href="https://fonts.googleapis.com/css2?family=PT+Sans:wght@400;700&family=Roboto:wght@400;700&family=Russo+One&display=swap">
<style>
  :root {
    --stage: #262626;
    --paper: #ffffff;
    --green: #62bb46;
    --green-deep: #1f8a2a;
    --yellow: #fcc80f;
    --navy: #173a5a;
    --ink: #141414;
    --photo-dark: #0b1630;
    --photo-mid: #1d4a8c;
    --photo-light: #3f7fc8;
  }
  html, body {
    margin: 0;
    padding: 0;
    width: 1200px;
    height: 1200px;
    overflow: hidden;
    background: var(--stage);
  }
  .canvas {
    position: relative;
    width: 1200px;
    height: 1200px;
  }
  .banner {
    position: absolute;
    left: 373px;
    top: 75px;
    width: 453px;
    height: 1050px;
    display: block;
  }
  .ribbon-text {
    font-family: "PT Sans", sans-serif;
    font-size: 27px;
    fill: var(--paper);
  }
  .brand-name {
    font-family: "Roboto", sans-serif;
    font-weight: 700;
    font-size: 50px;
    letter-spacing: 3px;
    fill: var(--ink);
  }
  .brand-tagline {
    font-family: "Russo One", sans-serif;
    font-size: 43px;
    fill: var(--green-deep);
  }
  .contact-title {
    font-family: "Roboto", sans-serif;
    font-weight: 700;
    font-size: 23px;
    fill: var(--paper);
  }
  .contact-line {
    font-family: "Roboto", sans-serif;
    font-size: 18px;
    fill: var(--paper);
  }
</style>
</head>
<body>
<main class="canvas">
  <svg class="banner" viewBox="0 0 566 1312" xmlns="http://www.w3.org/2000/svg">
    <defs>
      <linearGradient id="photoTone" x1="0" y1="0" x2="1" y2="1">
        <stop offset="0" stop-color="var(--photo-dark)"/>
        <stop offset="0.55" stop-color="var(--photo-mid)"/>
        <stop offset="1" stop-color="var(--photo-light)"/>
      </linearGradient>
    </defs>

    <rect class="banner-paper" x="0" y="0" width="566" height="1312" fill="var(--paper)"/>

    <polygon class="hero-photo" role="img"
      aria-label="Photo of a scientist in a white coat working on a large touchscreen with glowing blue data network graphics"
      points="0,0 566,0 566,579 0,769" fill="url(#photoTone)"/>

    <polygon class="ribbon ribbon-01" points="139,722 566,579 566,641 134,772" fill="var(--green)"/>
    <polygon class="ribbon ribbon-02" points="74,779 512,657 506,725 59,849" fill="var(--yellow)"/>
    <polygon class="ribbon ribbon-03" points="0,867 417,751 412,814 0,931" fill="var(--green)"/>

    <g class="ribbon-labels">
      <text class="ribbon-text" x="351" y="676" text-anchor="middle" transform="rotate(-17 351 676)">Enter text on this banner - 01</text>
      <text class="ribbon-text" x="276" y="764" text-anchor="middle" transform="rotate(-17 276 764)">Enter text on this banner - 02</text>
      <text class="ribbon-text" x="191" y="849" text-anchor="middle" transform="rotate(-17 191 849)">Enter text on this banner - 03</text>
    </g>

    <g class="brand">
      <circle class="brand-mark" cx="280" cy="944" r="66" fill="var(--green)"/>
      <text class="brand-name" x="280" y="1096" text-anchor="middle">HARBOR 3</text>
      <text class="brand-tagline" x="283" y="1162" text-anchor="middle">Data Discovery Studio</text>
    </g>

    <g class="contact-band">
      <rect x="0" y="1187" width="566" height="94" fill="var(--green)"/>
      <text class="contact-title" x="283" y="1229" text-anchor="middle">CONTACT US</text>
      <text class="contact-line" x="283" y="1259" text-anchor="middle">www.harbor-3.com | (0145) 555-210-384-00</text>
    </g>

    <rect class="base-band" x="0" y="1281" width="566" height="31" fill="var(--navy)"/>
  </svg>
</main>
</body>
</html>
```